Residential technology services business card

Looking for a simple, catchy, slightly fun business card design.

We are a residential technology service provider (computer repair, tablet repair, training, etc). We are a fun, upbeat, yet professional company that is very skilled at our job.

I will upload our logo in a sec, thinking that it should be the only thing on the front side of the card, with maybe a punch line as well... maybe not. Maybe the punchline can find a place on the back. You be the judge.

Backside should be minimal in terms of information. I need two variations: one that will only have our website and phone and one that will also include a persons name (and position), personal e-mail and personal phone.

Well, you're the designer, figure out the best way to place all above mentioned items.

Colors are white, black, green (as in logo), plus whatever else you think needs adding (if any).

It must be clear to people what we do (provide computer services, tablet services)... without using generic pictures of computers and tablets, unless it 's something original.

We want something original! But do note that the card will be printed on standard size business card paper, so no funky shapes please.

Thanks!!!

Requirements
Must have
• Logo, website, phone.
2nd variation also must include space for persons name, personal phone and email.

```html
<!DOCTYPE html>
<html lang="en">
<head>
<meta charset="utf-8">
<title>PixelPine Business Cards</title>
<link href="https://fonts.googleapis.com/css2?family=Ubuntu:wght@400;700&display=swap" rel="stylesheet">
<style>
  :root {
    --page: #e4e6e8;
    --card: #f1f1f1;
    --ink: #111111;
    --ink-soft: #444444;
    --band: #464646;
    --green: #7ab83a;
  }
  * { margin: 0; padding: 0; box-sizing: border-box; }
  html, body {
    width: 1200px;
    height: 1080px;
    overflow: hidden;
    background: var(--page);
    font-family: "Ubuntu", sans-serif;
  }
  .canvas {
    width: 1200px;
    height: 1080px;
    display: flex;
    flex-direction: column;
    align-items: center;
    justify-content: center;
    gap: 48px;
  }
  .card {
    position: relative;
    width: 840px;
    height: 480px;
    background: var(--card);
    box-shadow: 0 6px 18px rgba(0,0,0,0.18);
    overflow: hidden;
  }

  /* Front */
  .front__bar-black {
    position: absolute;
    left: 0;
    top: 38px;
    width: 52px;
    height: 160px;
    background: var(--ink);
  }
  .front__bar-green {
    position: absolute;
    right: 34px;
    top: 262px;
    width: 50px;
    height: 176px;
    background: var(--green);
  }
  .front__brand {
    position: absolute;
    left: 0;
    right: 0;
    top: 170px;
    text-align: center;
    font-weight: 700;
    font-size: 104px;
    letter-spacing: -3px;
    color: var(--ink);
  }

  /* Back */
  .back__band {
    position: absolute;
    left: 0;
    top: 0;
    width: 100%;
    height: 104px;
    background: var(--band);
  }
  .back__brand {
    position: absolute;
    left: 60px;
    top: 30px;
    font-weight: 700;
    font-size: 38px;
    letter-spacing: -1px;
    color: var(--ink);
  }
  .back__company-contact {
    position: absolute;
    right: 36px;
    top: 30px;
    text-align: right;
    font-size: 20px;
    line-height: 27px;
    letter-spacing: 1px;
    color: var(--green);
  }
  .back__name {
    position: absolute;
    left: 30px;
    top: 126px;
    font-size: 30px;
    letter-spacing: 1px;
    color: var(--ink);
  }
  .back__position {
    position: absolute;
    left: 132px;
    top: 166px;
    font-size: 24px;
    font-style: italic;
    letter-spacing: 1px;
    color: var(--ink-soft);
  }
  .back__personal-contact {
    position: absolute;
    right: 32px;
    bottom: 34px;
    text-align: right;
    font-size: 25px;
    line-height: 33px;
    letter-spacing: 1.5px;
    color: var(--ink);
  }
</style>
</head>
<body>
  <main class="canvas">
    <section class="card card--front" aria-label="Card front">
      <div class="front__bar-black"></div>
      <div class="front__bar-green"></div>
      <div class="front__brand">PixelPine</div>
    </section>

    <section class="card card--back" aria-label="Card back">
      <div class="back__band"></div>
      <div class="back__brand">PixelPine</div>
      <div class="back__company-contact">
        <div>Phone : 000-000-0000</div>
        <div>www.pixelpineny.com</div>
      </div>
      <div class="back__name">Your Name</div>
      <div class="back__position">position</div>
      <div class="back__personal-contact">
        <div>Home addres</div>
        <div>Phone : 000-000-0000</div>
        <div>personalemail@pixelpineny.com</div>
      </div>
    </section>
  </main>
</body>
</html>
```